Threads By Omar Design

We are a screen printing and embroidering company on apparel We also offer a full line of marketing products. I sell into virtually anyone who has these needs, however, my current card states Corporate and Athletic Apparel supplier. I want that changed to Custom Apparel and Promotional Solutions. I do a lot of work for local organizations and governments.

Target Market(s)

athletic organizations, school organizations, businesses anyone who buys apparel pretty wide open

Industry/Entity Type

Screen Printing

Contact Information for Business Card

My logo, Company Name, Name and title, address, phone email and website and facebook page

Colors

Designer to choose colors to be used in the design.

Requirements
Must have
• I would like the card to have a picture of an embroidering machine very light in the background or something depicting what I do. Maybe a side picture, not of me.

I want a glossy card
Should not have
• I do not want the information on the card to get lost

```html
<!DOCTYPE html>
<html lang="en">
<head>
<meta charset="utf-8">
<title>Threads By Omar – Business Card</title>
<link rel="stylesheet" href="https://fonts.googleapis.com/css2?family=Cabin:ital,wght@0,400;0,500;0,600;0,700;1,400&family=Playfair+Display:wght@900&display=swap">
<style>
  :root {
    --page: #ffffff;
    --card-light: #e9e9e7;
    --band-grey: #a9a9a9;
    --band-top: #dcdcda;
    --stitch: #f4f4f4;
    --ink: #1e1e1e;
    --ink-soft: #3a3a3a;
    --brand-red: #e3191f;
    --badge: #6b6b6b;
    --photo-dark: #8f8a84;
    --photo-mid: #c9c5c0;
  }
  * { margin: 0; padding: 0; box-sizing: border-box; }
  html, body { width: 1200px; height: 1200px; overflow: hidden; background: var(--page); }
  body { position: relative; font-family: "Cabin", "Gill Sans", sans-serif; color: var(--ink); }

  .card {
    position: absolute; left: 349px; top: 162px; width: 502px; height: 876px;
    background: linear-gradient(180deg, var(--band-top) 0, var(--card-light) 40%, #e4e4e2 100%);
    overflow: hidden;
  }
  .header-band {
    position: absolute; left: 0; top: 66px; width: 100%; height: 168px;
    background: linear-gradient(90deg, #b3b3b3, var(--band-grey));
  }
  .footer-band {
    position: absolute; left: 0; top: 732px; width: 100%; height: 144px;
    background: linear-gradient(90deg, #b0b0b0, var(--band-grey));
  }
  .stitch-line {
    position: absolute; left: 0; width: 100%; height: 0;
    border-top: 1.5px dashed var(--stitch);
  }
  .stitch-line.top { top: 84px; }
  .stitch-line.mid { top: 234px; }
  .stitch-line.bottom { top: 746px; }

  .machine-photo {
    position: absolute; left: 0; top: 234px; width: 300px; height: 498px;
    background:
      radial-gradient(ellipse 120px 180px at 60px 120px, var(--photo-dark), transparent 75%),
      radial-gradient(ellipse 200px 120px at 170px 300px, var(--photo-mid), transparent 80%);
    opacity: 0.75;
  }

  .brand {
    position: absolute; right: 31px; top: 96px; text-align: right;
    color: var(--brand-red); font-weight: 700; line-height: 1;
  }
  .brand .brand-main { display: block; font-size: 76px; letter-spacing: 2px; }
  .brand .brand-sub { display: block; font-size: 34px; margin-top: 8px; }

  .right { position: absolute; right: 31px; text-align: right; white-space: nowrap; line-height: 1; }
  .tagline { font-size: 25px; letter-spacing: 1.5px; color: var(--ink); }
  .tagline .amp { font-weight: 700; color: var(--ink-soft); }
  .person-name { font-family: "Playfair Display", serif; font-weight: 900; font-size: 34px; color: var(--brand-red); letter-spacing: 2px; }
  .person-title { font-size: 24px; font-style: italic; letter-spacing: 1px; color: var(--ink-soft); }
  .address { font-size: 24px; letter-spacing: 1.5px; color: var(--ink-soft); line-height: 34px; }
  .contact { font-size: 24px; display: flex; align-items: center; justify-content: flex-end; gap: 8px; }
  .contact.phone { font-weight: 600; letter-spacing: 1.5px; }
  .contact.email { letter-spacing: 0.5px; }
  .contact.web { font-size: 26px; font-weight: 600; letter-spacing: 1px; }
  .contact.social { font-size: 26px; letter-spacing: 0.5px; }
  .badge { width: 22px; height: 22px; flex: none; }
  .badge text { font-family: "Playfair Display", serif; font-weight: 900; font-size: 13px; fill: #fff; }
</style>
</head>
<body>
  <main class="card">
    <div class="header-band"></div>
    <div class="footer-band"></div>
    <div class="stitch-line top"></div>
    <div class="stitch-line mid"></div>
    <div class="stitch-line bottom"></div>

    <div class="machine-photo" role="img" aria-label="Faint photo of an embroidery machine presser foot stitching a leaf pattern on white fabric"></div>

    <div class="brand">
      <span class="brand-main">THREADS</span>
      <span class="brand-sub">by Omar</span>
    </div>

    <p class="right tagline" style="top:285px">CUSTOM APPAREL <span class="amp">&amp;</span></p>
    <p class="right tagline" style="top:327px">PROMOTIONAL SOLUTIONS</p>

    <p class="right person-name" style="top:414px">OMAR</p>
    <p class="right person-title" style="top:455px">OWNER</p>

    <p class="right address" style="top:554px">48 Mill Lane East,<br>Oak Harbor, IL 60412</p>

    <p class="right contact phone" style="top:641px">
      <svg class="badge" viewBox="0 0 22 22" aria-hidden="true"><path d="M2 2h18v10a9 9 0 0 1-9 9H2z" fill="var(--badge)"/><text x="11" y="16" text-anchor="middle">T</text></svg>
      555-204-7731
    </p>
    <p class="right contact email" style="top:682px">
      <svg class="badge" viewBox="0 0 22 22" aria-hidden="true"><path d="M2 2h18v10a9 9 0 0 1-9 9H2z" fill="var(--badge)"/><text x="11" y="16" text-anchor="middle">E</text></svg>
      omar@threadsbyomar.com
    </p>

    <p class="right contact web" style="top:769px">
      <svg class="badge" viewBox="0 0 22 22" aria-hidden="true"><path d="M2 2h18v10a9 9 0 0 1-9 9H2z" fill="var(--badge)"/><text x="11" y="16" text-anchor="middle">W</text></svg>
      threadsbyomar.com
    </p>
    <p class="right contact social" style="top:815px">
      <svg class="badge" viewBox="0 0 22 22" aria-hidden="true"><circle cx="11" cy="11" r="10" fill="var(--badge)"/></svg>
      social/threadsbyomar
    </p>
  </main>
</body>
</html>
```